KRV Boltline Manufacturer New Web Design

We need a new theme designed for metal fastener manufacturing company, KRV Boltline Group, a $60M division of Marlow Forge Holdings, Inc. We manufacture screw, pins and washers to industrial customers (non-Automotive) such as Hollis Appliance, Carl Whitby, BRN, Venmark, etc. Our current website is www.boltline-example.com. We would like to stick with the same logo/color scheme, however, I'm aiming to modernize the website's look and feel.

Here are some of our competitor's websites:
- https://www.quorvane.example/
- http://pindrovex.example/
- http://www.harlowbuiltjoinery.example/
- http://clivetandparts.example/
- http://www.dunmerebolt.example/

Target Market(s)

We primarily want to target engineers working in the following markets:
- Appliance (Hollis Appliance, Vannoria)
- Ag (Whitby, BRN)
- Recreational Vehicle (Venmark, Glade Runner)
- Outdoor Power (Brenholt, Mivo)

We secondarily want to target buyers working at the above markets as well as buyers at Fastener distributors such as Quillory, Provender Systems, Kessel Orwin.

Industry/Entity Type

Metal Forging

Number of Pages Required

1 page

Requirements
Must have
• For products: "Threaded" product as the primary focus. "Pins" product is the secondary focus, followed by all others.
• Please use same logo and color scheme as I do not plan to change.
Nice to have
• Highlight our featured proprietary products (pamphlets attached). KRV Boltline's GRI-Z, MelDowel, Boltline Helix, Blizzard.

```html
<!DOCTYPE html>
<html lang="en">
<head>
<meta charset="utf-8">
<title>KRV Boltline Group</title>
<link href="https://fonts.googleapis.com/css2?family=Open+Sans:wght@400;600;700&family=Roboto:wght@300;400;500;700&display=swap" rel="stylesheet">
<style>
:root{
  --brand:#1b6fa3;
  --brand-dark:#0f4d76;
  --navy:#123a57;
  --navy-deep:#0c2c44;
  --ink:#2d2d2d;
  --muted:#6b6f73;
  --line:#e3e6e8;
  --paper:#ffffff;
  --mist:#f3f4f5;
  --hero-a:#1b1d20;
  --hero-b:#3b3e42;
}
*{box-sizing:border-box;margin:0;padding:0}
html,body{width:1200px;height:2504px;overflow:hidden}
body{font-family:"Open Sans",Arial,sans-serif;color:var(--ink);background:var(--paper);font-size:12px;position:relative}
.wrap{width:720px;margin:0 auto;position:relative}
h2,h3,.nav,.btn{font-family:"Roboto",Arial,sans-serif}

/* header + hero */
.hero{height:470px;position:relative;overflow:hidden;background:radial-gradient(ellipse at 55% 50%,var(--hero-b),var(--hero-a) 70%)}
.hero-photo{position:absolute;inset:0;background:linear-gradient(180deg,rgba(255,255,255,.06),rgba(0,0,0,.25))}
.topbar{position:absolute;top:0;left:0;right:0;height:44px;background:rgba(0,0,0,.45);display:flex;align-items:center;padding:0 232px}
.logo{display:flex;align-items:center;gap:8px;color:#fff;font-family:"Roboto",sans-serif;font-weight:700;font-size:15px}
.logo-dot{width:18px;height:18px;border-radius:50%;background:var(--brand)}
.nav{margin-left:auto;display:flex;gap:22px;font-size:10px;color:#d6d8da}
.nav .active{color:#fff;border-bottom:2px solid var(--brand);padding-bottom:3px}
.nav-search{width:12px;height:12px}
.slide-labels{position:absolute;top:140px;left:0;right:0;display:flex;justify-content:center;align-items:center}
.slide-labels span{font-family:"Roboto",sans-serif;font-weight:300;letter-spacing:2px;font-size:30px;color:rgba(255,255,255,.25);position:absolute}
.slide-labels .l{left:180px}
.slide-labels .r{left:880px}
.slide-labels .c{color:#fff;font-weight:400;font-size:32px;position:static}
.hero-item{position:absolute;left:540px;top:210px;width:120px;height:110px;border-radius:6px;background:linear-gradient(135deg,#b9bcbf,#55595d)}
.hero-arrows{position:absolute;left:560px;top:398px;display:flex;gap:26px}
.hero-arrows svg{width:16px;height:16px}

/* products */
.section-title{text-align:center;font-size:22px;font-weight:400;color:var(--ink)}
.title-rule{width:40px;height:2px;background:var(--brand);margin:10px auto 14px}
.products{height:430px;padding-top:58px}
.lead{text-align:center;width:360px;margin:0 auto;color:var(--muted);font-size:11px;line-height:17px}
.cards{display:flex;gap:16px;margin-top:40px}
.card{width:168px;height:180px;border:1px solid var(--line);box-shadow:0 2px 6px rgba(0,0,0,.08);background:#fff}
.card-img{height:112px;margin:10px;border-radius:2px}
.card h3{font-size:12px;font-weight:500;padding:2px 12px}
.card .more{font-size:9px;color:var(--muted);padding:4px 12px;display:flex;align-items:center;gap:6px}
.more i{display:inline-block;width:18px;height:2px;background:var(--brand)}

/* video */
.video{height:160px;position:relative}
.video-frame{position:absolute;left:360px;top:0;width:480px;height:150px;background:linear-gradient(100deg,#2a2b2d,#4a4c4f 50%,#1e1f21)}
.play{position:absolute;left:50%;top:50px;transform:translateX(-50%);width:40px;height:40px;border-radius:50%;border:2px solid #fff;display:flex;align-items:center;justify-content:center}
.play-label{position:absolute;left:0;right:0;top:104px;text-align:center;color:#fff;font-family:"Roboto",sans-serif;font-size:14px}

/* engineering */
.engineering{height:430px;background:var(--mist);padding-top:90px}
.eng-head{display:flex;justify-content:space-between;align-items:center}
.eng-head h2{font-size:20px;font-weight:400}
.eng-arrows{display:flex;gap:12px}
.eng-rule{width:40px;height:2px;background:var(--brand);margin:8px 0 16px}
.eng-body{display:flex;justify-content:space-between}
.eng-text{width:430px}
.eng-text .strong{font-weight:700;color:var(--brand-dark);font-size:11px;line-height:16px;margin-bottom:10px}
.eng-text p{font-size:10px;line-height:16px;color:var(--muted);margin-bottom:8px}
.eng-photo{width:230px;height:170px;background:linear-gradient(135deg,#4e7c9c,#1c3d57);margin-top:8px}
.btn{display:inline-block;background:var(--brand-dark);color:#fff;font-size:10px;padding:8px 16px;margin-top:10px}

/* help band */
.help{height:150px;background:linear-gradient(90deg,var(--brand-dark),var(--brand));position:relative;padding-top:30px}
.help h2{color:#fff;font-size:18px;font-weight:400}
.help p{color:#cfe0ec;font-size:10px;line-height:15px;width:460px;margin-top:8px}
.help .btn{position:absolute;right:0;top:32px;background:transparent;border:1px solid #fff}

/* blog */
.blog{height:420px;padding-top:60px}
.posts{display:flex;gap:24px;margin-top:20px}
.post{width:224px}
.post-img{height:110px}
.post h3{font-size:11px;font-weight:500;line-height:16px;margin-top:10px;color:var(--ink)}
.post .more{font-size:9px;color:var(--muted);margin-top:6px;display:flex;align-items:center;gap:6px}

/* footer */
.footer-top{height:260px;background:var(--navy);color:#cfd9e1;padding-top:50px}
.locs{display:flex;justify-content:space-between}
.loc{width:170px}
.loc h3{color:#fff;font-size:13px;font-weight:400;margin-bottom:6px}
.loc .rule{width:26px;height:2px;background:var(--brand);margin-bottom:14px}
.loc .row{display:flex;gap:8px;font-size:9px;line-height:13px;margin-bottom:10px}
.loc svg{flex:0 0 10px;width:10px;height:10px;margin-top:2px}
.footer-main{height:200px;background:var(--navy-deep);color:#aebdc9;padding-top:30px}
.cols{display:flex;justify-content:space-between}
.col h3{color:#fff;font-size:14px;font-weight:400;margin-bottom:6px}
.col .rule{width:26px;height:2px;background:var(--brand);margin-bottom:14px}
.col p{font-size:9px;line-height:14px}
.about{width:220px}
.links{width:200px;display:grid;grid-template-columns:1fr 1fr;font-size:9px;line-height:18px}
.news{width:220px}
.news .item{font-size:9px;margin-bottom:10px}
.news .date{color:#7f93a3;font-size:8px;margin-top:3px}
.socials{display:flex;gap:12px;justify-content:flex-end;margin-top:20px}
.socials span{width:10px;height:10px;border-radius:50%;background:#7f93a3}
.copy{height:24px;background:#09223a;color:#7f93a3;font-size:8px;line-height:24px}
</style>
</head>
<body>

<header class="hero">
  <div class="hero-photo" role="img" aria-label="Dark studio photograph of threaded fasteners"></div>
  <div class="topbar">
    <div class="logo"><span class="logo-dot"></span>KRV Boltline</div>
    <nav class="nav">
      <span class="active">Home</span><span>Products</span><span>Capabilities</span><span>Engineering</span><span>Quality</span><span>Careers</span><span>Contact Us</span>
      <svg class="nav-search" viewBox="0 0 12 12"><circle cx="5" cy="5" r="3.5" fill="none" stroke="#fff" stroke-width="1.4"/><line x1="7.6" y1="7.6" x2="11" y2="11" stroke="#fff" stroke-width="1.4"/></svg>
    </nav>
  </div>
  <div class="slide-labels">
    <span class="l">STAMPINGS</span>
    <span class="c">THREADED</span>
    <span class="r">LOCK WASHERS</span>
  </div>
  <div class="hero-item" role="img" aria-label="Threaded bolt product shot"></div>
  <div class="hero-arrows">
    <svg viewBox="0 0 16 16"><path d="M11 3 5 8l6 5" fill="none" stroke="#fff" stroke-width="1.5"/></svg>
    <svg viewBox="0 0 16 16"><path d="M5 3l6 5-6 5" fill="none" stroke="#fff" stroke-width="1.5"/></svg>
  </div>
</header>

<section class="products">
  <h2 class="section-title">Our Products</h2>
  <div class="title-rule"></div>
  <p class="lead">KRV Boltline Group is a leading designer and manufacturer of value-added, high quality engineered hardware solutions.</p>
  <div class="wrap cards">
    <div class="card"><div class="card-img" role="img" aria-label="Lock washers" style="background:linear-gradient(135deg,#d9dadb,#6e7175)"></div><h3>Lock Washers</h3><div class="more"><i></i>View More</div></div>
    <div class="card"><div class="card-img" role="img" aria-label="Pins" style="background:linear-gradient(135deg,#e6e6e6,#a94848)"></div><h3>Pins</h3><div class="more"><i></i>View More</div></div>
    <div class="card"><div class="card-img" role="img" aria-label="Stampings" style="background:linear-gradient(135deg,#eceded,#8b8e92)"></div><h3>Stampings</h3><div class="more"><i></i>View More</div></div>
    <div class="card"><div class="card-img" role="img" aria-label="Threaded fasteners" style="background:linear-gradient(135deg,#f0f0f0,#7c8086)"></div><h3>Threaded</h3><div class="more"><i></i>View More</div></div>
  </div>
</section>

<section class="video">
  <div class="video-frame" role="img" aria-label="Video still of the production floor">
    <div class="play"><svg width="14" height="14" viewBox="0 0 14 14"><path d="M4 2l8 5-8 5z" fill="#fff"/></svg></div>
    <div class="play-label">Play Video</div>
  </div>
</section>

<section class="engineering">
  <div class="wrap">
    <div class="eng-head">
      <h2>Engineering</h2>
      <div class="eng-arrows">
        <svg width="12" height="12" viewBox="0 0 12 12"><path d="M8 2 4 6l4 4" fill="none" stroke="#999" stroke-width="1.4"/></svg>
        <svg width="12" height="12" viewBox="0 0 12 12"><path d="M4 2l4 4-4 4" fill="none" stroke="#999" stroke-width="1.4"/></svg>
      </div>
    </div>
    <div class="eng-rule"></div>
    <div class="eng-body">
      <div class="eng-text">
        <p class="strong">KRV Boltline Group engineers are highly trained in the science of fastening.</p>
        <p>Our team works closely with customers from the first sketch through final production, reviewing joint design, materials and assembly methods to reduce cost and improve reliability.</p>
        <p>Our engineers use advanced modeling and in-house testing to validate every part, checking clamp load, torque and fatigue before a single production run begins on our lines.</p>
        <p>To learn how our team can support your next program, contact KRV Boltline Group today and speak with an applications engineer.</p>
        <span class="btn">View More</span>
      </div>
      <div class="eng-photo" role="img" aria-label="Engineer working at a laboratory test station"></div>
    </div>
  </div>
</section>

<section class="help">
  <div class="wrap">
    <h2>How Can We Help You?</h2>
    <p>If you have a question regarding a product, pricing or design support, please reach out and one of our team members will respond shortly.</p>
    <span class="btn">Get In Touch</span>
  </div>
</section>

<section class="blog">
  <h2 class="section-title">Our Blog</h2>
  <div class="title-rule"></div>
  <div class="wrap posts">
    <div class="post"><div class="post-img" role="img" aria-label="Heavy agricultural equipment at a worksite" style="background:linear-gradient(135deg,#d8b16a,#6d6a62)"></div><h3>KRV Boltline Leading Midwest Fastener Solutions</h3><div class="more"><i style="display:inline-block;width:18px;height:2px;background:var(--brand)"></i>View More</div></div>
    <div class="post"><div class="post-img" role="img" aria-label="Assorted bolts and screws" style="background:linear-gradient(135deg,#eeeeee,#7a7d82)"></div><h3>KRV Boltline Leading Midwest Fastener Solutions</h3><div class="more"><i style="display:inline-block;width:18px;height:2px;background:var(--brand)"></i>View More</div></div>
    <div class="post"><div class="post-img" role="img" aria-label="Close view of threaded fasteners" style="background:linear-gradient(135deg,#c9ccd0,#4d5055)"></div><h3>KRV Boltline Leading Midwest Fastener Solutions</h3><div class="more"><i style="display:inline-block;width:18px;height:2px;background:var(--brand)"></i>View More</div></div>
  </div>
</section>

<footer>
  <div class="footer-top">
    <div class="wrap locs">
      <div class="loc"><h3>Stampings</h3><div class="rule"></div>
        <div class="row"><svg viewBox="0 0 10 10"><path d="M5 1a3 3 0 0 1 3 3c0 2.2-3 5-3 5S2 6.2 2 4a3 3 0 0 1 3-3z" fill="#5a9bc6"/></svg>1410 Orchard Lane, Elgin IL 60120</div>
        <div class="row"><svg viewBox="0 0 10 10"><path d="M2 1h2l1 2-1 1a5 5 0 0 0 2 2l1-1 2 1v2c-4 1-8-3-7-7z" fill="#5a9bc6"/></svg>(630) 555-0142</div>
        <div class="row"><svg viewBox="0 0 10 10"><rect x="1" y="2" width="8" height="6" fill="none" stroke="#5a9bc6"/><path d="M1 2l4 3 4-3" fill="none" stroke="#5a9bc6"/></svg>stampings@boltline-example.com</div></div>
      <div class="loc"><h3>Pins</h3><div class="rule"></div>
        <div class="row"><svg viewBox="0 0 10 10"><path d="M5 1a3 3 0 0 1 3 3c0 2.2-3 5-3 5S2 6.2 2 4a3 3 0 0 1 3-3z" fill="#5a9bc6"/></svg>88 Mill Creek Road, Dayton OH 45402</div>
        <div class="row"><svg viewBox="0 0 10 10"><path d="M2 1h2l1 2-1 1a5 5 0 0 0 2 2l1-1 2 1v2c-4 1-8-3-7-7z" fill="#5a9bc6"/></svg>(630) 555-0178</div>
        <div class="row"><svg viewBox="0 0 10 10"><rect x="1" y="2" width="8" height="6" fill="none" stroke="#5a9bc6"/><path d="M1 2l4 3 4-3" fill="none" stroke="#5a9bc6"/></svg>pins@boltline-example.com</div></div>
      <div class="loc"><h3>Lock Washers</h3><div class="rule"></div>
        <div class="row"><svg viewBox="0 0 10 10"><path d="M5 1a3 3 0 0 1 3 3c0 2.2-3 5-3 5S2 6.2 2 4a3 3 0 0 1 3-3z" fill="#5a9bc6"/></svg>22 Foundry Way, Rockdale IL 60436</div>
        <div class="row"><svg viewBox="0 0 10 10"><path d="M2 1h2l1 2-1 1a5 5 0 0 0 2 2l1-1 2 1v2c-4 1-8-3-7-7z" fill="#5a9bc6"/></svg>(630) 555-0193</div>
        <div class="row"><svg viewBox="0 0 10 10"><rect x="1" y="2" width="8" height="6" fill="none" stroke="#5a9bc6"/><path d="M1 2l4 3 4-3" fill="none" stroke="#5a9bc6"/></svg>washers@boltline-example.com</div></div>
      <div class="loc"><h3>Threaded</h3><div class="rule"></div>
        <div class="row"><svg viewBox="0 0 10 10"><path d="M5 1a3 3 0 0 1 3 3c0 2.2-3 5-3 5S2 6.2 2 4a3 3 0 0 1 3-3z" fill="#5a9bc6"/></svg>305 Harbor Street, Joliet IL 60432</div>
        <div class="row"><svg viewBox="0 0 10 10"><path d="M2 1h2l1 2-1 1a5 5 0 0 0 2 2l1-1 2 1v2c-4 1-8-3-7-7z" fill="#5a9bc6"/></svg>(630) 555-0127</div>
        <div class="row"><svg viewBox="0 0 10 10"><rect x="1" y="2" width="8" height="6" fill="none" stroke="#5a9bc6"/><path d="M1 2l4 3 4-3" fill="none" stroke="#5a9bc6"/></svg>sales@boltline-example.com</div></div>
    </div>
  </div>
  <div class="footer-main">
    <div class="wrap cols">
      <div class="col about"><h3>About Us</h3><div class="rule"></div>
        <p>Known as KRV Boltline Group today, the roots of the company reach back to the 1930s with a focus on engineered fasteners. The business joined Marlow Forge Holdings, Inc. in the 1970s.</p></div>
      <div class="col"><h3>Quick Links</h3><div class="rule"></div>
        <div class="links"><span>Home</span><span>Quality</span><span>Products</span><span>About Us</span><span>Capabilities</span><span>Careers</span><span>Engineering</span><span>Contact</span></div></div>
      <div class="col news"><h3>Recent News</h3><div class="rule"></div>
        <div class="item">KRV Boltline Expands Midwest Production<div class="date">August 9, 2017</div></div>
        <div class="item">KRV Boltline Leading Midwest Fastener Solutions<div class="date">August 2, 2017</div></div>
        <div class="socials"><span></span><span></span><span></span></div></div>
    </div>
  </div>
  <div class="copy"><div class="wrap">© 2017 KRV Boltline Group · Terms &amp; Conditions</div></div>
</footer>

</body>
</html>
```